依頼詳細
A社より添付の案を頂いているのですが、①グループ会社である安心感親近感をアピールしたい②メリット1のA社専用のプランを他のメリットよりも強調したいと思い、依頼をさせて頂く事となりました。
注意点、会社案内欄の箇所は空白でお願い致します。
社名を変更して今後活用したいので、パワーポイントでの納品をお願い致します。
記載項目
株式会社ZAT/03-4817-2935/https://www.za-t.jp/
サイズ
A4
ページ数
片面
希望イメージ
シンプル 複雑
単色 カラフル
暗い 明るい
日常 高級
遊び心 厳粛
未来的 伝統的
女性的 男性的
希望する色
納品ファイル
補足説明
■ 選んだ理由

社員の選定を元に選ばせて頂きました。親近感があるという意見が多かったです。

■ 提案者全員のお礼・コメント

締め切りが近い中多数のご応募頂きありがとうございます。またご機会ありましたら宜しくお願い致します。

```html
<!DOCTYPE html>
<html lang="ja">
<head>
<meta charset="utf-8">
<title>専用火災保険のご案内</title>
<link href="https://fonts.googleapis.com/css2?family=Noto+Sans+JP:wght@400;500;700;900&display=swap" rel="stylesheet">
<style>
:root{
  --yellow:#f6c400;
  --yellow-soft:#fff4c2;
  --cream:#fffbea;
  --orange:#ee7b00;
  --ink:#333333;
  --blank:#d6d6d6;
  --white:#ffffff;
  --illust-warm:#fbe3a0;
  --illust-cool:#cfe3ee;
}
*{box-sizing:border-box;margin:0;padding:0}
html,body{width:846px;height:1200px;overflow:hidden;background:var(--white)}
body{font-family:"Noto Sans JP",sans-serif;color:var(--ink);position:relative}
.abs{position:absolute}
.blank{background:var(--blank);border-radius:3px}
.illust{border-radius:12px}

.period-tag{left:560px;top:20px;width:266px;height:32px;border:2px solid var(--ink);font-size:15px;font-weight:500;display:flex;align-items:center;justify-content:center}
.family{left:30px;top:44px;width:218px;height:236px;background:linear-gradient(180deg,var(--yellow) 0%,var(--illust-warm) 55%,var(--cream) 100%);border-radius:110px 110px 16px 16px}

.intro-line{right:28px;font-size:21px;font-weight:700;white-space:nowrap}
.headline{right:28px;top:264px;font-size:40px;font-weight:900;color:var(--orange);letter-spacing:1px;white-space:nowrap}

.merit{border:4px solid var(--yellow);border-radius:12px;background:var(--white)}
.merit-label{position:absolute;left:-4px;top:-4px;background:var(--yellow);border-radius:10px 0 10px 0;width:62px;height:62px;display:flex;flex-direction:column;align-items:center;justify-content:center;line-height:1}
.merit-label small{font-size:11px;font-weight:700}
.merit-label b{font-size:32px;font-weight:900}

.m1{left:22px;top:333px;width:508px;height:434px}
.m2{left:541px;top:333px;width:283px;height:434px}
.m3{left:22px;top:784px;width:294px;height:330px}
.m4{left:327px;top:784px;width:248px;height:330px}
.m5{left:587px;top:784px;width:237px;height:330px}

.owner{left:80px;top:20px;display:flex;align-items:center;gap:8px;font-size:30px;font-weight:900}
.owner .blank{width:200px;height:36px}
.plan{left:36px;top:76px;width:430px;text-align:center;font-size:52px;font-weight:900;color:var(--orange);background:linear-gradient(transparent 62%,var(--yellow-soft) 62%)}
.price-box{left:36px;top:160px;width:430px;height:112px;background:var(--yellow-soft);border-radius:10px;display:flex;align-items:center;gap:18px;padding:0 20px}
.yen{width:70px;height:70px;border-radius:50%;background:var(--yellow);flex:none}
.price-text{font-size:30px;font-weight:900;line-height:1.25;color:var(--orange)}
.price-text small{display:block;font-size:14px;color:var(--ink);font-weight:500;text-align:right}
.price-text span{color:var(--ink)}
.houses{left:36px;top:292px;width:430px;height:120px;background:linear-gradient(90deg,var(--illust-cool),var(--illust-warm))}

.m2 .lead{left:70px;top:20px;font-size:26px;font-weight:900;line-height:1.35}
.m2 .lead em{font-style:normal;color:var(--orange)}
.docs{left:50px;top:150px;width:175px;height:115px;background:linear-gradient(180deg,var(--illust-cool),var(--white))}
.direct{left:16px;top:290px;width:250px;font-size:20px;font-weight:700;line-height:2;white-space:nowrap}
.direct .blank{display:inline-block;vertical-align:middle;height:28px}

.m3 .who{left:76px;top:16px;display:flex;align-items:center;gap:6px;font-size:24px;font-weight:900}
.m3 .who .blank{width:160px;height:32px}
.m3 .role{left:14px;top:66px;font-size:24px;font-weight:900;white-space:nowrap}
.stat-cap{font-size:14px;font-weight:700;left:14px}
.stat{left:14px;width:258px;height:40px;background:var(--yellow-soft);border-radius:6px;display:flex;align-items:center;padding-left:14px;font-size:16px;font-weight:700}
.stat b{font-size:30px;font-weight:900;color:var(--orange);margin-left:4px}
.m3 .note{left:14px;top:282px;width:260px;font-size:11px;line-height:1.5}

.calendar{left:104px;top:18px;width:80px;height:74px;background:var(--illust-warm)}
.m4 .big{left:0;width:100%;text-align:center;top:108px;font-size:28px;font-weight:900;color:var(--orange)}
.m4 .sub{left:0;width:100%;text-align:center;top:150px;font-size:20px;font-weight:900}
.body-text{font-size:16px;font-weight:500;line-height:1.75;text-align:center}
.m4 .body-text{left:14px;top:206px;width:212px}

.m5 .big{left:0;width:100%;text-align:center;top:68px;font-size:26px;font-weight:900;color:var(--orange)}
.m5 .sub{left:0;width:100%;text-align:center;top:106px;font-size:20px;font-weight:900}
.clock{left:148px;top:14px;width:56px;height:56px;border-radius:50%;background:var(--illust-warm)}
.m5 .body-text{left:14px;top:206px;width:202px}

.footer{left:22px;top:1130px;width:802px;height:52px;border-top:2px solid var(--yellow);display:flex;align-items:center;gap:26px;padding-top:8px}
.brand{display:flex;align-items:center;gap:8px;font-size:24px;font-weight:900;color:var(--orange)}
.brand i{width:22px;height:22px;border-radius:50%;background:var(--yellow);display:block}
.footer .info{font-size:15px;font-weight:500;white-space:nowrap}
.footer .url{margin-left:auto}
</style>
</head>
<body>
  <div class="abs period-tag">2021年1月以降保険始期用</div>
  <div class="abs family illust" role="img" aria-label="家の前に立つ家族のイラスト"></div>

  <div class="abs blank" style="left:268px;top:58px;width:262px;height:28px"></div>
  <p class="abs intro-line" style="top:94px">の住宅購入されるお客さまへ</p>
  <div class="abs blank" style="left:268px;top:146px;width:166px;height:26px"></div>
  <p class="abs intro-line" style="top:142px">より下記提携代理店をご紹介します。</p>
  <div class="abs blank" style="left:324px;top:218px;width:324px;height:36px"></div>
  <p class="abs intro-line" style="left:656px;right:auto;top:216px;font-size:28px;font-weight:900">より</p>
  <h1 class="abs headline">専用火災保険のご案内です。</h1>

  <section class="abs merit m1">
    <div class="merit-label"><small>メリット</small><b>1</b></div>
    <div class="abs owner"><span class="blank"></span>オーナーさま</div>
    <p class="abs plan">専用プラン適用!</p>
    <div class="abs price-box">
      <div class="yen" role="img" aria-label="円マークのアイコン"></div>
      <p class="price-text">割安な保険料で<small>(地震保険は除く)</small><span>ご契約いただけます。</span></p>
    </div>
    <div class="abs houses illust" role="img" aria-label="並んだ住宅のイラスト"></div>
  </section>

  <section class="abs merit m2">
    <div class="merit-label"><small>メリット</small><b>2</b></div>
    <p class="abs lead">ご契約時<br>お建物資料等の<br><em>ご提出不要!</em></p>
    <div class="abs docs illust" role="img" aria-label="書類のイラスト"></div>
    <p class="abs direct"><span class="blank" style="width:110px"></span> と <span class="blank" style="width:92px"></span><br><span class="blank" style="width:110px"></span> で<br>直接やりとりいたします。</p>
  </section>

  <section class="abs merit m3">
    <div class="merit-label"><small>メリット</small><b>3</b></div>
    <div class="abs who"><span class="blank"></span>は</div>
    <p class="abs role">火災保険専門代理店</p>
    <p class="abs stat-cap" style="top:108px">2019年度お取扱実績</p>
    <div class="abs stat" style="top:132px">約<b>3,500</b>件</div>
    <p class="abs stat-cap" style="top:190px">2020年8月時点保有契約件数</p>
    <div class="abs stat" style="top:214px">約<b>28,000</b>件</div>
    <p class="abs note">多くのお客さまにご支持いただいております。</p>
  </section>

  <section class="abs merit m4">
    <div class="merit-label"><small>メリット</small><b>4</b></div>
    <div class="abs calendar illust" role="img" aria-label="カレンダーのイラスト"></div>
    <p class="abs big">土日祝日も</p>
    <p class="abs sub">ご案内いたします!</p>
    <p class="abs body-text">お客様のご都合の<br>良い日時にご案内<br>させていただきます。</p>
  </section>

  <section class="abs merit m5">
    <div class="merit-label"><small>メリット</small><b>5</b></div>
    <div class="abs clock" role="img" aria-label="時計のイラスト"></div>
    <p class="abs big">スピーディーな</p>
    <p class="abs sub">お申込手続き!</p>
    <p class="abs body-text">最短で当日から<br>補償開始のお手続き<br>が可能です。</p>
  </section>

  <footer class="abs footer">
    <div class="brand"><i></i>ZAT</div>
    <p class="info">株式会社ZAT　TEL:03-4817-2935</p>
    <p class="info url">https://www.za-t.jp/</p>
  </footer>
</body>
</html>
```